BRIGHT COLORFUL + 55 FAMILY HISTORY BROCHURE 11 x 17 bifold

11 x 17 Bifold Flyer I have given you the Layout I just need you to make it Pretty

YOU DO NOT NEED TO FOLLOW MY LAYOUT, You can but dont have too

Target Market(s)

55 year old consumers, who could choose our service of Hereditary Cancer Screening

Industry/Entity Type

Health And Wellness

Requirements
Must have
• Must be appealing to Grand Parents, must make them want to test , show lots of pictures of grand children, YOU DO NOT NEED TO FOLLOW MY LAYOUT , You can but dont have too
Nice to have
• use our colors of our logo , YOU DO NOT NEED TO FOLLOW MY LAYOUT , You can but dont have too
Should not have
• YOU DO NOT NEED TO FOLLOW MY LAYOUT, You can but dont have too

```html
<!DOCTYPE html>
<html lang="en">
<head>
<meta charset="utf-8">
<title>Hereditary Cancer Screening – Bifold Brochure</title>
<link rel="stylesheet" href="https://fonts.googleapis.com/css2?family=Marcellus&family=Tinos:ital,wght@0,400;0,700;1,400;1,700&family=Kaushan+Script&display=swap">
<style>
  :root{
    --navy:#14235c;
    --navy-deep:#0c1740;
    --green:#8cbf1e;
    --green-bright:#a3cf2a;
    --green-text:#6ea312;
    --ink:#2b2b2b;
    --paper:#ffffff;
    --stage:#dcdcdc;
    --photo-warm:#d9b99a;
    --photo-light:#efe4d6;
    --photo-green:#9fb877;
  }
  *{box-sizing:border-box;margin:0;padding:0}
  html,body{width:1200px;height:675px;overflow:hidden}
  body{background:var(--stage);font-family:"Tinos",serif;color:var(--ink);position:relative}

  .spread{position:absolute;top:156px;width:560px;height:362px;display:flex;background:var(--paper)}
  .spread--outside{left:26px}
  .spread--inside{left:614px}
  .panel{position:relative;width:280px;height:362px;overflow:hidden}

  .photo{position:absolute;display:block}
  .footer-band{position:absolute;left:0;bottom:0;width:100%;height:32px;background:var(--green);display:flex;align-items:center;justify-content:center}
  .url{font-family:"Tinos",serif;font-size:7px;font-weight:700;color:var(--paper);letter-spacing:.2px}

  .brand{display:flex;align-items:center;gap:5px;justify-content:center}
  .brand__dot{border-radius:50%;background:var(--navy)}
  .brand__name{font-family:"Tinos",serif;font-weight:700;color:var(--navy);line-height:1}

  /* back panel */
  .panel--back{background:linear-gradient(180deg,#fff 0%,#fff 48%,#f2f8df 62%,#b9dc55 82%,var(--green) 100%)}
  .back__title{position:absolute;top:16px;left:20px;font-size:9.5px;font-weight:700;color:var(--navy)}
  .back__tagline{position:absolute;top:32px;right:16px;width:150px;text-align:right;font-size:8.5px;color:var(--green-text);line-height:1.15}
  .back__lead{position:absolute;top:64px;left:16px;right:16px;text-align:center;font-size:7px;font-weight:700;color:var(--navy);line-height:1.25}
  .back__copy{position:absolute;left:18px;right:18px;text-align:center;font-size:6px;color:var(--green-text);line-height:1.3}
  .back__copy--one{top:104px}
  .back__copy--two{top:146px}
  .photo-grid{position:absolute;top:180px;left:16px;width:248px;display:grid;grid-template-columns:repeat(4,1fr);gap:3px}
  .photo-grid .tile{height:50px;border:1.5px solid var(--green-bright)}
  .panel--back .brand{position:absolute;left:0;right:0;top:300px}

  /* front cover */
  .cover__header{position:absolute;top:0;left:0;width:100%;height:58px;background:linear-gradient(180deg,var(--navy-deep),var(--navy) 70%,#5a6a95)}
  .cover__title{position:absolute;top:14px;width:100%;text-align:center;font-family:"Marcellus",serif;font-size:17px;color:var(--paper)}
  .cover__subtitle{position:absolute;top:36px;width:100%;text-align:center;font-family:"Tinos",serif;font-style:italic;font-size:7.5px;color:#d8e8a8}
  .cover__question{position:absolute;top:181px;left:14px;right:14px;text-align:center;font-size:8.5px;font-weight:700;color:var(--navy);line-height:1.2}
  .cover__question span{background:rgba(255,255,255,.8);padding:0 2px}
  .cover__tab{position:absolute;top:208px;left:60px;width:160px;height:34px;background:var(--navy);border-radius:0 0 26px 26px;display:flex;align-items:center;justify-content:center;text-align:center;color:var(--paper);font-size:7.5px;line-height:1.2}
  .cover__rule{position:absolute;top:204px;left:0;width:100%;height:4px;background:var(--navy)}
  .cover__script{position:absolute;top:250px;width:100%;text-align:center;font-family:"Kaushan Script",cursive;font-size:9.5px;color:var(--green-text);line-height:1.3}
  .panel--front .brand{position:absolute;left:0;right:0;top:286px}

  /* inside */
  .story{position:absolute;left:18px;right:18px;font-size:4.6px;line-height:1.32;text-align:justify;color:var(--ink)}
  .story b{color:var(--ink)}
  .story p{margin-bottom:4px}
  .story p:first-line{}
  .caption{position:absolute;left:0;right:0;text-align:center;font-family:"Tinos",serif;font-style:italic;font-weight:700;font-size:6px;color:var(--navy);line-height:1.35}
  .caption span{background:rgba(255,255,255,.75);padding:0 2px}
  .callout{position:absolute;left:14px;right:14px;top:140px;text-align:center;font-family:"Tinos",serif;font-style:italic;font-weight:700;font-size:8px;color:var(--navy);line-height:1.4}
</style>
</head>
<body>

<section class="spread spread--outside" aria-label="Brochure outside spread">
  <article class="panel panel--back">
    <h2 class="back__title">DOES CANCER Run in Your Family?</h2>
    <p class="back__tagline">A Simple Swab Could SAVE a Family Members LIFE</p>
    <p class="back__lead">Your decision won't just affect you. It will also impact Your Family, since your test results may Forecast Their Cancer Risks, too.</p>
    <p class="back__copy back__copy--one">We believe it is important to understand what can and cannot be learned with genetic testing. Genetic mutations can increase risks for certain cancers, but this does not mean cancer will definitely develop. You should be prepared to receive positive or negative results.</p>
    <p class="back__copy back__copy--two">Most people receive Negative Results meaning no mutations associated with an increased risk for the Hereditary cancers.</p>
    <div class="photo-grid">
      <div class="tile" role="img" aria-label="Grandmother hugging a grandchild" style="background:linear-gradient(135deg,var(--photo-light),var(--photo-warm))"></div>
      <div class="tile" role="img" aria-label="Grandparents with grandchildren" style="background:linear-gradient(135deg,#e8ddd0,#b9a48c)"></div>
      <div class="tile" role="img" aria-label="Grandfather playing with a grandchild outdoors" style="background:linear-gradient(135deg,#d7e2c0,var(--photo-warm))"></div>
      <div class="tile" role="img" aria-label="Smiling grandmother with grandchild" style="background:linear-gradient(135deg,#c69a78,#7a5a44)"></div>
      <div class="tile" role="img" aria-label="Grandmother embracing two grandchildren" style="background:linear-gradient(135deg,#e4c9b2,#a77e60)"></div>
      <div class="tile" role="img" aria-label="Three generations of a family together" style="background:linear-gradient(135deg,#dbe6c6,#c39e80)"></div>
      <div class="tile" role="img" aria-label="Grandfather laughing" style="background:linear-gradient(135deg,#d8bfa6,#8e6f58)"></div>
      <div class="tile" role="img" aria-label="Grandfather reading with a grandchild" style="background:linear-gradient(135deg,#cfd9c3,var(--photo-green))"></div>
    </div>
    <div class="brand">
      <span class="brand__dot" style="width:11px;height:11px"></span>
      <span class="brand__name" style="font-size:8px">KINWARD HEALTH GROUP</span>
    </div>
    <div class="footer-band" style="background:transparent"><span class="url">www.kinwardscreening.com</span></div>
  </article>

  <article class="panel panel--front">
    <div class="photo" role="img" aria-label="Three-generation family smiling together outdoors" style="top:40px;left:0;width:280px;height:164px;background:linear-gradient(180deg,#7f8fa8 0%,#d8c6b0 35%,#caa888 70%,#b89a80 100%)"></div>
    <div class="cover__header"></div>
    <h1 class="cover__title">Hereditary Cancer Screening</h1>
    <p class="cover__subtitle">"The Test You Take For Them"</p>
    <p class="cover__question"><span>Will You give Your loved ones</span><br><span>the information to Beat Cancer in their lives?</span></p>
    <div class="cover__rule"></div>
    <div class="cover__tab">Give Them the Gift<br>of Knowledge</div>
    <p class="cover__script">Knowing is better than not knowing.<br>Knowledge is Power</p>
    <div class="brand">
      <span class="brand__dot" style="width:22px;height:22px"></span>
      <span class="brand__name" style="font-size:13px">KINWARD<br>HEALTH GROUP</span>
    </div>
    <div class="footer-band"><span class="url">www.kinwardscreening.com</span></div>
  </article>
</section>

<section class="spread spread--inside" aria-label="Brochure inside spread">
  <article class="panel">
    <div class="story" style="top:16px">
      <p>Genetic testing revealed Martin Ellery carried a mutation that gave him a 55 to 70 percent chance of developing stomach cancer. Early screening revealed there were 14 sites of stage 1A cancer. Once the news sunk in, he realized <b>his Mother Genetic Testing Saved His Life.</b></p>
      <p><b>Genetic Testing Saved My Life.</b> Because of my age and <b>family ancestry</b>, my doctor recommended Genetic Testing and they were right. I had the BRCA Gene, because of this my other two sisters got tested, my younger sister was positive and my older sister was negative. Now we are in control, there are steps that can be taken to reduce the risks, including enhanced breast cancer screening, risk-reducing surgeries, and chemoprevention, in which drugs are used to try to reduce the risk or delay the development of cancer.</p>
      <p>A breast cancer survivor before age 30: 'Genetic testing saved my life' Dana Whitfield was diagnosed with breast cancer two weeks before her 29th birthday. Now 30, she credits her recovery to <b>awareness of a hereditary genetic mutation</b> that predisposed her and her family to the disease. <b>After my mom tested positive for the BRCA 1 gene mutation</b>, I knew genetic testing was something that I would need. <b>Once I tested positive</b>, I was referred to a breast health clinic for increased surveillance. There, my medical care providers were very diligent in making sure I was watched closely. <b>Knowledge is power</b> and, in this case, <b>Genetic testing saved my life!</b></p>
      <p>My father had <b>genetic testing</b> and found he had hereditary nonpolyposis colorectal cancer (HNPCC) commonly known as Lynch syndrome. My name is Helen Marsh and I am a 10-year survivor of colorectal cancer. From an early age I learned the importance of screenings and knew about signs and symptoms. <b>Following screening guidelines for individuals at an increased risk &amp; Knowing my family history saved my life!</b></p>
    </div>
    <div class="photo" role="img" aria-label="Grandparents sitting with grandchildren on a sofa" style="top:222px;left:0;width:280px;height:108px;background:linear-gradient(135deg,#f1ebe2 0%,#d9c4ad 45%,#b4b8c8 100%)"></div>
    <p class="caption" style="top:292px"><span>A Positive result or finding a mutation is Not a Cancer Diagnosis</span><br><span>and does not mean you will ever develop Cancer</span><br><span>learning if you have an increased risk for cancer can make a difference</span></p>
    <div class="footer-band"><span class="url">www.kinwardscreening.com</span></div>
  </article>

  <article class="panel">
    <div class="story" style="top:16px">
      <p>Genetic Testing is done to determine whether family members without obvious illness have inherited the same mutation as a family member who is known to carry a cancer associated mutation. Meaning <b>Will You Help Your Kids &amp; Grand Children.</b></p>
      <p><b>What are the benefits of testing?</b> "The Power of Knowledge" Helping <b>Younger Family Members Know if there is a Risk and Preparing for it.</b> Knowing if you have a genetic mutation is that you can work with your doctor to monitor and address your cancer risks. <b>According to the National Wellness Council eating 5 or more Servings of Vegetables &amp; Fruit, and Most Importantly also lowering your intake of red meat, dairy and eggs will help prevent or delay cancer.</b></p>
      <p><b>There are many benefits to getting tested</b>, regardless of the eventual result. If one of your family members — however distant — had cancer, there is a chance that you inherited a gene mutation that not only increases your personal risk of cancer, but also could be passed to the next generation. Those who are carriers of hereditary cancer gene mutations could be at risk of getting cancer earlier in life than the general population. <b>The sooner genetic testing is done, the more likely it is that the risk can be managed appropriately.</b></p>
    </div>
    <p class="callout">There are many Known risk factors for Cancer.<br>GENETICS and FAMILY HISTORY are Often Overlooked.</p>
    <div class="photo" role="img" aria-label="Grandparents relaxing on a sofa with two grandchildren" style="top:178px;left:0;width:280px;height:152px;background:linear-gradient(135deg,#f4efe8 0%,#e2d3c2 40%,#bfc9d2 100%)"></div>
    <div class="footer-band"><span class="url">www.kinwardscreening.com</span></div>
  </article>
</section>

</body>
</html>
```